Looking for a cool, modern Cannabis Jar Label

I want you to come up with a better, modern look for a label.

I need it sized to 4” x 3” - I plan to print directly to label printer.

I want you to use Photoshop and deliver me a layered PSD file that I can edit and modify the information as needed..

The label information will need to include places for:
(1) Strain Name - most important part of label - larger font size than rest - example Kelvin Thistle, TRP #7, Copperleaf Dunes
(2) Pricing - for Gram, 1/8, 1/4, 1/2. and Ounce
(3) Strain Designation (Hybrid, Indica or Sativa) - maybe color coded, different color for Indica v. Sativa, just an idea
(4) THC and CBD percentages - for example 23% THC and 0.05% CBD
(5) Farm name - a place where we can add the name/logo of the business that produced the product. example - Brosk Farms

I have attached a simple mockup showing the information.

I have also attached a few samples of labels we like to give you an idea of the look and feel we are going for.

I am wanting a very clean, modern, classy, readable look.The font will use is Gotham Font.

HI Everyone! Thank you for all of your designs. I am requesting an extension because I need more time to give adequate feedback to the designers. Thank you for your participation and all of your efforts! I will be making a decision soon!

• Gotham Font

• Thank you for your designs. I am sorry i have been slow in providing feedback, things have been really busy around here!
• I wanted to give some group general feedback. After reviewing all of the designs, there is a common theme among all of the designs that I would like to see changed.
• I would like to see the per gram pricing more prominent on the label. This is what most people are looking for when they are purchasing the product. So I would like to see this stand out from the other pricing tiers. As I think about it, they don't all need to be grouped together in a line. You could have the Per Gram pricing front and center some where and then the other pricing tiers grouped together somewhere else on the label.
• This is the order of importance of items on the label. Items at the the top of the list should be bigger than those below it.
• 1. Strain name
• 2. Pricing - being per gram the most important of all prices
• 3. THC/CBD percentages
• 4. Strain Type (indica, sativa, hybrid)
• 5. Farm name/logo
• When laying out these labels, they will be going on rounded jars and they will be on display. Think of jars with fancy labels in a candy store. They need to be eye catchy, appealing, but easy read.
• Thank you for all of your hard work, everyone is doing a great job.
• Best,
• Neta

```html
<!DOCTYPE html>
<html lang="en">
<head>
<meta charset="utf-8">
<title>Cannabis Jar Labels</title>
<link rel="stylesheet" href="https://fonts.googleapis.com/css2?family=Montserrat:wght@400;500;700;800&family=Roboto+Condensed:wght@300;400&display=swap">
<style>
  :root {
    --backdrop: #b8b4af;
    --paper: #ffffff;
    --ink: #1b1b1b;
    --muted: #555555;
    --tag-grey: #4d4d4d;
    --sativa: #e0336a;
    --indica: #1f6a35;
    --hybrid: #a8901c;
    --logo-green: #2f8a3c;
    --warning-red: #d8232a;
  }
  * { box-sizing: border-box; margin: 0; padding: 0; }
  html, body { width: 1200px; height: 1200px; overflow: hidden; }
  body {
    background: var(--backdrop);
    font-family: "Montserrat", Arial, sans-serif;
    color: var(--ink);
    position: relative;
  }
  .label {
    position: absolute;
    width: 540px;
    height: 405px;
    background: var(--paper);
    box-shadow: 0 4px 14px rgba(0,0,0,0.18);
  }
  .label--sativa { --accent: var(--sativa); left: 40px; top: 120px; }
  .label--indica { --accent: var(--indica); left: 620px; top: 120px; }
  .label--hybrid { --accent: var(--hybrid); left: 330px; top: 640px; }

  .title-box {
    position: absolute; left: 18px; top: 18px; width: 504px; height: 128px;
    border: 4px solid var(--accent); border-radius: 20px;
    display: flex; flex-direction: column; align-items: center; justify-content: center;
  }
  .strain-name { font-size: 54px; font-weight: 400; letter-spacing: 0.5px; line-height: 1; }
  .label--hybrid .strain-name { font-size: 48px; margin-top: -10px; }
  .strain-cross { font-size: 28px; font-weight: 400; margin-top: 6px; }
  .type-tag {
    position: absolute; top: 132px; left: 50%; transform: translateX(-50%);
    background: var(--accent); color: #fff;
    font-size: 24px; font-weight: 400; letter-spacing: 1px;
    height: 32px; line-height: 32px; padding: 0 24px;
  }

  .prices {
    position: absolute; left: 18px; top: 176px; width: 504px;
    display: flex; justify-content: space-between;
  }
  .price { text-align: center; font-family: "Roboto Condensed", Arial Narrow, sans-serif; }
  .price-amount { font-size: 38px; font-weight: 400; line-height: 1; white-space: nowrap; letter-spacing: -1px; }
  .price-cents { font-size: 19px; vertical-align: 15px; text-decoration: underline; letter-spacing: 0; }
  .price-unit { font-family: "Montserrat", Arial, sans-serif; font-size: 16px; color: var(--muted); margin-top: 1px; }

  .potency-box {
    position: absolute; left: 18px; top: 244px; width: 168px; height: 146px;
    border: 1.5px solid var(--ink); padding: 8px 8px 0;
  }
  .potency-row { display: flex; justify-content: space-between; }
  .potency { width: 72px; text-align: center; }
  .potency-value {
    font-family: "Roboto Condensed", Arial Narrow, sans-serif;
    font-size: 36px; line-height: 1; letter-spacing: -1px;
  }
  .potency-value small { font-size: 18px; letter-spacing: 0; }
  .potency-tag {
    background: var(--tag-grey); color: #fff; font-size: 19px; margin-top: 4px;
    height: 26px; line-height: 26px;
  }
  .activation {
    font-size: 8.5px; font-weight: 700; margin-top: 8px; padding-bottom: 3px;
    border-bottom: 1px solid var(--ink);
  }
  .test-info { font-size: 7.5px; font-weight: 700; line-height: 1.45; margin-top: 4px; }

  .grower-panel {
    position: absolute; left: 198px; top: 244px; width: 210px; height: 146px;
    border-top: 1.5px solid var(--ink); border-bottom: 1.5px solid var(--ink);
    text-align: center; padding-top: 8px;
  }
  .product-kind { font-size: 13px; font-weight: 700; }
  .cultivated { font-size: 13px; margin-top: 4px; }
  .farm-mark {
    display: flex; align-items: center; justify-content: center; gap: 10px;
    margin: 12px 0 10px;
  }
  .farm-square { width: 30px; height: 30px; background: var(--logo-green); border-radius: 4px; }
  .farm-name { font-size: 22px; font-weight: 800; color: var(--ink); letter-spacing: 0.5px; }
  .harvest { font-size: 8px; font-weight: 700; line-height: 1.6; }

  .warning-box {
    position: absolute; left: 418px; top: 244px; width: 104px; height: 146px;
    border: 1.5px solid var(--ink); padding: 6px 5px;
  }
  .warning-text { font-size: 6.6px; font-weight: 700; line-height: 1.4; text-transform: uppercase; }
  .warning-symbol {
    position: absolute; left: 50%; bottom: 7px; transform: translateX(-50%);
    width: 40px; height: 40px; border: 2px solid var(--ink); background: var(--warning-red);
  }
</style>
</head>
<body>

<!-- Sativa label -->
<section class="label label--sativa">
  <div class="title-box"><h1 class="strain-name">Ruby Canyon</h1></div>
  <div class="type-tag">SATIVA</div>
  <div class="prices">
    <div class="price"><div class="price-amount">€ 10<span class="price-cents">.50</span></div><div class="price-unit">Gram</div></div>
    <div class="price"><div class="price-amount">€ 35<span class="price-cents">.00</span></div><div class="price-unit">1/8</div></div>
    <div class="price"><div class="price-amount">€ 70<span class="price-cents">.00</span></div><div class="price-unit">1/4</div></div>
    <div class="price"><div class="price-amount">€ 140<span class="price-cents">.00</span></div><div class="price-unit">1/2</div></div>
    <div class="price"><div class="price-amount">€ 280<span class="price-cents">.00</span></div><div class="price-unit">Ounce</div></div>
  </div>
  <div class="potency-box">
    <div class="potency-row">
      <div class="potency"><div class="potency-value">22<small>%</small></div><div class="potency-tag">THC</div></div>
      <div class="potency"><div class="potency-value">0.07<small>%</small></div><div class="potency-tag">CBD</div></div>
    </div>
    <p class="activation">Activation time: &nbsp;Immediately</p>
    <p class="test-info">Tested by: Lorem Ipsum<br>No. ref: 1234567890123456<br>Test Date:</p>
  </div>
  <div class="grower-panel">
    <p class="product-kind">Cannabis Flower</p>
    <p class="cultivated">Cultivated By:</p>
    <div class="farm-mark"><span class="farm-square"></span><span class="farm-name">VERDANT ROW</span></div>
    <p class="harvest">Harvest Date:<br>Batch No. 1234567890123456</p>
  </div>
  <div class="warning-box">
    <p class="warning-text">Keep out of reach of children and animals. Cannabis products may only be possessed or consumed by persons 21 years of age or older unless the person is a qualified patient.</p>
    <div class="warning-symbol" role="img" aria-label="Cannabis warning symbol"></div>
  </div>
</section>

<!-- Indica label -->
<section class="label label--indica">
  <div class="title-box"><h1 class="strain-name">Kelvin Thistle</h1></div>
  <div class="type-tag">INDICA</div>
  <div class="prices">
    <div class="price"><div class="price-amount">€ 10<span class="price-cents">.50</span></div><div class="price-unit">Gram</div></div>
    <div class="price"><div class="price-amount">€ 35<span class="price-cents">.00</span></div><div class="price-unit">1/8</div></div>
    <div class="price"><div class="price-amount">€ 70<span class="price-cents">.00</span></div><div class="price-unit">1/4</div></div>
    <div class="price"><div class="price-amount">€ 140<span class="price-cents">.00</span></div><div class="price-unit">1/2</div></div>
    <div class="price"><div class="price-amount">€ 280<span class="price-cents">.00</span></div><div class="price-unit">Ounce</div></div>
  </div>
  <div class="potency-box">
    <div class="potency-row">
      <div class="potency"><div class="potency-value">25<small>%</small></div><div class="potency-tag">THC</div></div>
      <div class="potency"><div class="potency-value">0.05<small>%</small></div><div class="potency-tag">CBD</div></div>
    </div>
    <p class="activation">Activation time: &nbsp;Immediately</p>
    <p class="test-info">Tested by: Lorem Ipsum<br>No. ref: 1234567890123456<br>Test Date:</p>
  </div>
  <div class="grower-panel">
    <p class="product-kind">Cannabis Flower</p>
    <p class="cultivated">Cultivated By:</p>
    <div class="farm-mark"><span class="farm-square"></span><span class="farm-name">VERDANT ROW</span></div>
    <p class="harvest">Harvest Date:<br>Batch No. 1234567890123456</p>
  </div>
  <div class="warning-box">
    <p class="warning-text">Keep out of reach of children and animals. Cannabis products may only be possessed or consumed by persons 21 years of age or older unless the person is a qualified patient.</p>
    <div class="warning-symbol" role="img" aria-label="Cannabis warning symbol"></div>
  </div>
</section>

<!-- Hybrid label -->
<section class="label label--hybrid">
  <div class="title-box">
    <h1 class="strain-name">Harbor Sourleaf</h1>
    <p class="strain-cross">Pixie x Mist</p>
  </div>
  <div class="type-tag">HYBRID</div>
  <div class="prices">
    <div class="price"><div class="price-amount">€ 10<span class="price-cents">.50</span></div><div class="price-unit">Gram</div></div>
    <div class="price"><div class="price-amount">€ 35<span class="price-cents">.00</span></div><div class="price-unit">1/8</div></div>
    <div class="price"><div class="price-amount">€ 70<span class="price-cents">.00</span></div><div class="price-unit">1/4</div></div>
    <div class="price"><div class="price-amount">€ 140<span class="price-cents">.00</span></div><div class="price-unit">1/2</div></div>
    <div class="price"><div class="price-amount">€ 280<span class="price-cents">.00</span></div><div class="price-unit">Ounce</div></div>
  </div>
  <div class="potency-box">
    <div class="potency-row">
      <div class="potency"><div class="potency-value">29.5<small>%</small></div><div class="potency-tag">THC</div></div>
      <div class="potency"><div class="potency-value">0.04<small>%</small></div><div class="potency-tag">CBD</div></div>
    </div>
    <p class="activation">Activation time: &nbsp;10-15 minutes</p>
    <p class="test-info">Tested by: Lorem Ipsum<br>No. ref: 1234567890123456<br>Test Date:</p>
  </div>
  <div class="grower-panel">
    <p class="product-kind">Cannabis Flower</p>
    <p class="cultivated">Cultivated By:</p>
    <div class="farm-mark"><span class="farm-square"></span><span class="farm-name">VERDANT ROW</span></div>
    <p class="harvest">Harvest Date:<br>Batch No. 1234567890123456</p>
  </div>
  <div class="warning-box">
    <p class="warning-text">Keep out of reach of children and animals. Cannabis products may only be possessed or consumed by persons 21 years of age or older unless the person is a qualified patient.</p>
    <div class="warning-symbol" role="img" aria-label="Cannabis warning symbol"></div>
  </div>
</section>

</body>
</html>
```